Modern and Improved business card design for Family Dental Practice

We have 2 sets of logo we have designed and now just need a business card layout and design for the office. Colors are on the logo. We can choose which logo we want to go with . The font can be changed to whatever seems modern and relevant. We are family dental office that has been open for over 15 years in South Austin Texas.

Target Market(s)

Handout Business cards to referrals and specialists

Industry/Entity Type

Dental

Contact Information for Business Card

We need address, phone, website and email address. 4870 North Loop Rd Suite 208 , Austin,Texas 78651....phone: 512-480-7319.....email- info@maplebrookdental-example.com....website - MapleBrookDental-example.com

Font styles to use
Serif
Decorative

Requirements
Must have
• my logo. We have 2 logos, but we can use just one or if we can incorporate one on one side and the other on the other side.
Nice to have
• Really just need a modern look and clean that incorporates the logo and colors .

```html
<!DOCTYPE html>
<html lang="en">
<head>
<meta charset="utf-8">
<title>Maple Brook Family Dentistry – Business Card</title>
<link href="https://fonts.googleapis.com/css2?family=Didact+Gothic&display=swap" rel="stylesheet">
<style>
  :root {
    --stage: #2b2b2b;
    --card: #ffffff;
    --ink: #111111;
    --green: #0f7a1c;
    --green-soft: #8aa52b;
    --card-shadow: rgba(0,0,0,0.45);
  }
  * { box-sizing: border-box; margin: 0; padding: 0; }
  html, body {
    width: 1200px; height: 1056px; overflow: hidden;
    background: var(--stage);
    font-family: "Didact Gothic", "Century Gothic", sans-serif;
    color: var(--ink);
  }
  .sheet {
    width: 1200px; height: 1056px;
    display: flex; flex-direction: column; align-items: center;
    justify-content: center; gap: 40px;
  }
  .card {
    position: relative;
    width: 840px; height: 480px;
    background: var(--card);
    box-shadow: 0 14px 36px var(--card-shadow);
    overflow: hidden;
  }
  .brand-name {
    text-transform: uppercase; color: var(--ink);
    font-weight: 400; line-height: 0.98; letter-spacing: 1px;
  }
  .brand-name .tagline {
    display: block; letter-spacing: 3px; margin-top: 10px; line-height: 1.1;
  }

  /* Front */
  .front .brand-mark {
    position: absolute; left: 70px; top: 70px;
    width: 340px; height: 340px; border-radius: 50%;
    background: var(--green);
  }
  .front .brand-name {
    position: absolute; right: 70px; top: 80px;
    text-align: right; font-size: 58px;
  }
  .front .brand-name .tagline { font-size: 22px; }
  .contact {
    position: absolute; right: 70px; top: 262px;
    text-align: right; font-size: 17px; line-height: 1.35;
    list-style: none;
  }
  .contact li { display: flex; justify-content: flex-end; align-items: center; gap: 12px; }
  .contact li + li { margin-top: 8px; }
  .contact .address { display: block; margin-bottom: 6px; }
  .icon {
    width: 24px; height: 24px; border-radius: 4px;
    background: var(--green);
    display: inline-flex; align-items: center; justify-content: center;
    flex: none;
  }
  .icon svg { width: 16px; height: 16px; }

  /* Back */
  .back .wordmark {
    position: absolute; left: 50%; top: 50%;
    transform: translate(-50%, -50%);
    display: flex; align-items: center; gap: 24px;
  }
  .back .brand-dot {
    width: 110px; height: 110px; border-radius: 50%;
    background: var(--green);
  }
  .back .brand-name { font-size: 50px; }
  .back .brand-name .tagline { font-size: 20px; }
</style>
</head>
<body>
<main class="sheet">

  <section class="card front" aria-label="Business card front">
    <span class="brand-mark"></span>
    <h1 class="brand-name">Maple<br>Brook<span class="tagline">Family Dentistry</span></h1>
    <ul class="contact">
      <li class="address">4870 North Loop Rd Suite 208 , Austin<br>Texas 78651</li>
      <li>512-480-7319
        <span class="icon"><svg viewBox="0 0 16 16"><path d="M4 1.5l2.2 2.6-1.3 1.6c.8 2 2.4 3.6 4.4 4.4l1.6-1.3 2.6 2.2-1.4 2.2C7 12.8 3.2 9 1.8 3L4 1.5z" fill="#fff"/></svg></span>
      </li>
      <li>info@maplebrookdental-example.com
        <span class="icon"><svg viewBox="0 0 16 16"><rect x="2" y="4" width="12" height="8" fill="none" stroke="#fff" stroke-width="1.4"/><path d="M2 4l6 5 6-5" fill="none" stroke="#fff" stroke-width="1.4"/></svg></span>
      </li>
      <li>MapleBrookDental-example.com
        <span class="icon"><svg viewBox="0 0 16 16"><path d="M4 2l8 6-3.5.6 2 4-1.6.8-2-4L4 12z" fill="#fff"/></svg></span>
      </li>
    </ul>
  </section>

  <section class="card back" aria-label="Business card back">
    <div class="wordmark">
      <span class="brand-dot"></span>
      <h2 class="brand-name">Maple<br>Brook<span class="tagline">Family Dentistry</span></h2>
    </div>
  </section>

</main>
</body>
</html>
```